Hi, I need a clean, simple card to hand out to parents for my tutoring business (elementary). I would like the front of the card to have the moose logo below, reading a book. Back should be clean, centered text, no logo just information.

Target Market(s)

Elementary school parents

Industry/Entity Type

Tutoring

Contact Information for Business Card

Front of card:

Moose logo on left + text on right says "Bright Otter Tutoring"

Back of card:

MARA KOVIC
email envelope icon + BrightOtterTutoring@quillpost.net

Licensed Harwell Public Schools Teacher
Brennick University, M.S. Education

Font styles to use
Serif
Other font styles liked:
• Handwritten font for "Bright Otter Tutoring" and "Mara Kovic", all else should be serif font

Colors
fee18b
fdf9ce

Requirements
Must have
• Playful, clean, simple. Font listed below.

```html
<!DOCTYPE html>
<html lang="en">
<head>
<meta charset="utf-8">
<title>Bright Otter Tutoring – Business Card</title>
<link href="https://fonts.googleapis.com/css2?family=Gochi+Hand&family=Lora:wght@400;500&display=swap" rel="stylesheet">
<style>
  :root {
    --page-bg: #f4f4f4;
    --card-bg: #fdf9ce;
    --card-edge: #fee18b;
    --frame: #5a3a28;
    --ink: #4a2f20;
    --ink-soft: #6a4a36;
    --mark: #8a5a3c;
    --mark-warm: #fee18b;
  }
  * { margin: 0; padding: 0; box-sizing: border-box; }
  html, body { width: 1200px; height: 900px; overflow: hidden; }
  body {
    background: var(--page-bg);
    display: flex;
    align-items: center;
    justify-content: center;
    gap: 60px;
  }
  .card {
    position: relative;
    width: 520px;
    height: 300px;
    background: var(--card-bg);
    border: 3px solid var(--card-edge);
    border-radius: 26px;
    overflow: hidden;
    box-shadow: 0 14px 24px rgba(0, 0, 0, 0.12);
  }
  .card__frame {
    position: absolute;
    inset: 10px;
    border: 5px solid var(--frame);
    border-radius: 22px;
  }
  /* Front */
  .card--front .brand {
    position: absolute;
    inset: 0;
    display: flex;
    flex-direction: column;
    align-items: center;
    justify-content: center;
    gap: 14px;
  }
  .brand__mark {
    width: 120px;
    height: 120px;
    border-radius: 50%;
    background: radial-gradient(circle at 50% 40%, var(--mark) 0 58%, var(--mark-warm) 100%);
  }
  .brand__name {
    font-family: "Gochi Hand", cursive;
    font-size: 34px;
    color: var(--ink);
    letter-spacing: 0.5px;
    text-transform: uppercase;
  }
  /* Back */
  .back__info {
    position: absolute;
    left: 100px;
    right: 30px;
    top: 84px;
    text-align: center;
    font-family: "Lora", serif;
    color: var(--ink);
  }
  .back__name {
    font-family: "Gochi Hand", cursive;
    font-size: 30px;
    font-weight: 400;
    letter-spacing: 1px;
    line-height: 1.1;
  }
  .back__credentials {
    margin-top: 4px;
    font-size: 11.5px;
    line-height: 1.4;
    color: var(--ink-soft);
  }
  .back__email {
    margin-top: 24px;
    display: flex;
    align-items: center;
    justify-content: center;
    gap: 6px;
    font-size: 15px;
  }
  .back__email svg { width: 20px; height: 16px; flex: none; }
</style>
</head>
<body>
  <section class="card card--front" aria-label="Card front">
    <div class="card__frame"></div>
    <div class="brand">
      <div class="brand__mark" role="img" aria-label="Tutoring mascot illustration reading a book"></div>
      <div class="brand__name">Bright Otter Tutoring</div>
    </div>
  </section>

  <section class="card card--back" aria-label="Card back">
    <div class="card__frame"></div>
    <div class="back__info">
      <h1 class="back__name">MARA KOVIC</h1>
      <p class="back__credentials">Licensed Harwell Public Schools Teacher<br>Brennick University, M.S. Education</p>
      <p class="back__email">
        <svg viewBox="0 0 20 16" aria-hidden="true">
          <rect x="1" y="2" width="18" height="13" rx="1.5" fill="var(--mark)"/>
          <path d="M1.5 3 L10 9.5 L18.5 3" fill="none" stroke="var(--card-bg)" stroke-width="1.6"/>
        </svg>
        BrightOtterTutoring@quillpost.net
      </p>
    </div>
  </section>
</body>
</html>
```